Spiritual Web Design Project

I am looking to rebrand our www.GentleRiverGuidanceCollegeHub.example site to have a more spiritual look and feel (find out everything we do and offer at that site - have also uploaded picture of current site).
Photoshop format is fine and then we can have someone code it for our Wordpress site.
I want the site to have more movement and light to it (but static for our Wordpress site Don't want flash) I want the site to have a warmer, more ethereal feel to it.
I like the yellow, but think it needs more 'life' and a more spiritual feel. I am also thinking of changing to purple (see a sample attached - although this is a little too dark).
Maybe the banner should go the entire width of a webpage (like this): http://www.harwickstudio.example/speaking
or this: http://www.tidemoor.example/faqs
with a simple white background
I like this background (but not the dark blue)
http://www.calm-meadow.example/ I like this style of background, and I like this colour and style here: http://www.oakhollowpressworks.example/
I want our background to have more 'light and movement' in it.
I am thinking of changing our current font. I quite like the font here:
http://www.calm-meadow.example/
Also the two fonts attached - I like more depth (light and shade) in these than the one we have on our site now which looks quite flat
I've also attached a sample of some changes I have been looking at but I think there is too much purple
Again, I am not exactly sure what I want, but I will definately know it when I see it. The one thing I would like to keep is our 'flower graphic' on the left hand side. Also, maybe my photo could be incorporated somewhere - but not really sure if it needs to be
Once we have the branding of the site done, I want to re-brand everything else, all the resources, marketing materials etc.
Please don't submit before you look at the sites I have mentioned that I like and the attachments.
ALso I only need the Header Graphic and the Background of the site - we are doing the actual site ourselves - so I need a header and background only
Target Market(s)
Spirit-led women who are looking to start their own Law of Attraction Coaching Business
Industry/Entity Type
Marketing
Requirements
Should not have
- Flash
Should not be dark

```html
<!DOCTYPE html>
<html lang="en">
<head>
<meta charset="utf-8">
<title>Gentle River Guidance College</title>
<link href="https://fonts.googleapis.com/css2?family=PT+Sans:wght@400;700&family=Open+Sans:wght@400;600;700&family=Comfortaa:wght@400;700&family=Caveat:wght@600&display=swap" rel="stylesheet">
<style>
:root{
  --pink:#e1307b;
  --pink-dark:#a8184f;
  --pink-deep:#8e1442;
  --orange:#f07d12;
  --orange-box:#f29a14;
  --cyan:#1ec2ee;
  --header-dark:#0d2410;
  --text:#333;
  --grey-line:#bbb;
  --white:#fff;
}
*{margin:0;padding:0;box-sizing:border-box}
html,body{width:737px;height:1200px;overflow:hidden;background:var(--white)}
body{position:relative;font-family:'Open Sans',sans-serif;color:var(--text)}
.abs{position:absolute}

.site-header{left:0;top:0;width:737px;height:85px;background:radial-gradient(ellipse at 60% 0%,#2f5a22 0%,#16361a 45%,var(--header-dark) 100%)}
.brand{left:84px;top:20px;display:flex;align-items:center;gap:12px;color:var(--white);font-family:'Comfortaa',sans-serif}
.brand-dot{width:46px;height:46px;border-radius:50%;background:#5a4bc9}
.brand-name{font-size:22px;line-height:24px;font-weight:400}
.tagline{right:101px;top:28px;text-align:right;color:var(--white);font-family:'Comfortaa',sans-serif;font-size:8.5px;line-height:12px}
.search{left:531px;top:58px;width:105px;height:15px;background:var(--white);border-radius:2px;font-size:6.5px;padding:3px 6px;color:#555}
.search svg{position:absolute;right:3px;top:2px}

.main-nav{left:0;top:85px;width:737px;height:40px;background:var(--pink);display:flex;justify-content:center}
.main-nav a{color:var(--white);font-family:'PT Sans',sans-serif;font-weight:700;font-size:8.5px;text-decoration:none;line-height:40px;padding:0 27px;border-right:1px solid rgba(255,255,255,.25)}
.main-nav a:last-child{border-right:none}

.hero{left:0;top:125px;width:737px;height:263px;background:radial-gradient(ellipse at 50% 55%,#f07cc0 0%,#e457a5 22%,#8a3a6a 38%,#1d3a16 60%,#0c200b 100%)}
.hero-title{left:114px;top:168px;color:var(--white);font-family:'PT Sans',sans-serif;font-weight:700;font-size:19px;line-height:21px;text-shadow:0 1px 3px rgba(0,0,0,.5)}
.hero-sub{left:116px;top:227px;color:#cfeefa;font-family:'PT Sans',sans-serif;font-style:italic;font-size:15px;line-height:18px;text-shadow:0 1px 3px rgba(0,0,0,.6)}
.hero-arrow{top:233px;width:40px;height:40px;border-radius:50%;background:rgba(200,200,200,.75)}
.hero-dots{left:593px;top:362px;display:flex;gap:5px}
.hero-dots span{width:6px;height:6px;border-radius:50%;background:var(--white)}
.hero-dots span:first-child{background:transparent;border:1px solid var(--white)}

.intro-script{left:0;width:737px;text-align:center;color:var(--pink);font-family:'Caveat',cursive;font-size:28px;line-height:34px;top:411px}
.intro-question{left:0;top:493px;width:737px;text-align:center;color:var(--orange);font-family:'PT Sans',sans-serif;font-weight:700;font-size:18px;line-height:22px}
.rule{left:140px;width:453px;height:1px;background:var(--grey-line)}
.intro-answer{left:110px;top:562px;width:517px;text-align:center;font-size:13px;line-height:19px;color:#333}

.author-card{left:91px;top:634px;width:318px;height:151px;border:1px solid #ccc;border-radius:5px;overflow:hidden}
.ribbon{left:-22px;top:16px;width:100px;height:14px;background:var(--cyan);color:var(--white);font-size:6px;font-weight:700;text-align:center;line-height:14px;transform:rotate(-45deg)}
.author-photo{left:18px;top:19px;width:73px;height:110px;background:linear-gradient(160deg,#c9a27a,#e8e2da 55%,#7fb0c7)}
.author-name{left:105px;top:18px;color:var(--pink);font-family:'Caveat',cursive;font-size:19px}
.author-bio{left:105px;top:49px;width:190px;font-size:7.2px;line-height:12px;color:#444}
.read-more{left:244px;top:122px;width:57px;height:14px;background:var(--cyan);border-radius:3px;color:var(--white);font-size:7px;text-align:center;line-height:14px}

.video{left:418px;top:634px;width:230px;height:150px;border:3px solid #333;background:linear-gradient(180deg,#7fa94a,#3c6e22 60%,#2e4f1c)}
.video-play{left:97px;top:47px;width:44px;height:44px;border-radius:50%;background:rgba(40,40,40,.8)}
.video-caption{left:8px;top:113px;color:var(--white);font-family:'Open Sans',sans-serif;font-weight:600;font-size:17px;text-shadow:0 1px 3px rgba(0,0,0,.7)}

.solution{top:818px;width:130px;height:130px;border-radius:50%;background:var(--pink);color:var(--white);text-align:center}
.solution h3{font-family:'Open Sans',sans-serif;font-weight:400;font-size:13px;margin-top:24px}
.solution hr{border:none;height:1px;background:rgba(255,255,255,.5);width:84px;margin:6px auto 8px}
.solution p{font-size:7.5px;line-height:10px;width:100px;margin:0 auto}
.solution .more{display:block;width:54px;height:14px;margin:8px auto 0;background:var(--pink-deep);border-radius:4px;font-size:7.5px;line-height:14px}

.quote{top:980px;width:153px;height:84px;background:var(--orange-box);border-radius:4px;color:var(--white);font-size:7px;line-height:10px;padding:12px 10px}
.quote-tail{top:1063px}
.quote-name{top:1068px;font-size:7.5px;font-weight:700;color:#222}

.cta{left:427px;top:980px;width:219px;height:85px;border-radius:5px;background:linear-gradient(180deg,#f3b7cc,#c94a78 45%,#a82456);color:var(--white);box-shadow:0 3px 4px rgba(0,0,0,.25)}
.cta-small{left:16px;top:16px;font-size:9px}
.cta-big{left:16px;top:25px;font-size:15px;font-weight:600}
.cta-button{left:62px;top:55px;width:101px;height:20px;background:var(--pink-deep);border-radius:3px;font-size:14px;font-weight:700;text-align:center;line-height:20px}

.site-footer{left:0;top:1098px;width:737px;height:102px;background:var(--pink);color:var(--white)}
.footer-col{top:15px;font-size:6px;line-height:10px}
.social{left:541px;top:25px;display:flex;gap:8px}
.social span{width:15px;height:15px;border-radius:50%;background:#f3c7da}
.footer-links{left:93px;top:64px;font-size:7.5px}
.copyright{left:541px;top:64px;font-size:6px}
</style>
</head>
<body>

<header class="site-header abs">
  <div class="brand abs"><span class="brand-dot"></span><span class="brand-name">Gentle River<br>Guidance College</span></div>
  <p class="tagline abs">...delivering transformational coach training<br>and business success stories worldwide</p>
  <div class="search abs">Search
    <svg width="10" height="11" viewBox="0 0 10 11"><path d="M3 1l5 4.5L3 10" fill="none" stroke="#e1307b" stroke-width="2"/></svg>
  </div>
</header>

<nav class="main-nav abs">
  <a href="#">LIFE COACH TRAINING</a>
  <a href="#">SUCCESS STORIES</a>
  <a href="#">MEDIA &amp; AWARDS</a>
  <a href="#">CONTACT US</a>
  <a href="#">COACHES LOGIN</a>
</nav>

<section class="hero abs" role="img" aria-label="Close-up of a pink lotus flower against a dark green background"></section>
<h1 class="hero-title abs">JOIN TODAY AND RECEIVE AN<br>AMAZING BUNDLE OF BONUSES</h1>
<p class="hero-sub abs">Super Early Bird Pricing and be Ready<br>to Transform Your Life Forever!</p>
<div class="hero-arrow abs" style="left:44px">
  <svg width="40" height="40" viewBox="0 0 40 40"><path d="M23 11l-9 9 9 9" fill="none" stroke="#fff" stroke-width="2.5"/></svg>
</div>
<div class="hero-arrow abs" style="left:655px">
  <svg width="40" height="40" viewBox="0 0 40 40"><path d="M17 11l9 9-9 9" fill="none" stroke="#fff" stroke-width="2.5"/></svg>
</div>
<div class="hero-dots abs"><span></span><span></span><span></span></div>

<h2 class="intro-script abs">Do You Love ‘The Open Door’ and the Law of Attraction?<br>Want to Spend Your Days Becoming the Best You Can Be?</h2>
<p class="intro-question abs">Ready to Help Others Create an AMAZING Future<br>AND be Paid Abundantly to Do So?</p>
<div class="rule abs" style="top:551px"></div>
<p class="intro-answer abs">If you answered Yes – then your spirit will soar as you are about to discover how your life will be changed forever more.</p>
<div class="rule abs" style="top:610px"></div>

<article class="author-card abs">
  <div class="ribbon abs">ABOUT AUTHOR</div>
  <div class="author-photo abs" role="img" aria-label="Portrait photo of the author sitting outdoors"></div>
  <h3 class="author-name abs">Maren Ashby</h3>
  <p class="author-bio abs">Hi, my name is Maren Ashby and I've transformed my life and thousands of others by using these exact principles. I became an Accredited Coach in 2001 and have created a wonderfully fulfilling and successful coaching business by combining the Law of Attraction with masterful practical strategies.</p>
  <span class="read-more abs">READ MORE</span>
</article>

<div class="video abs" role="img" aria-label="Video still of a woman meditating on grass">
  <div class="video-play abs">
    <svg width="44" height="44" viewBox="0 0 44 44"><path d="M17 12l14 10-14 10z" fill="#fff"/></svg>
  </div>
  <span class="video-caption abs">Easy Steps for Success</span>
</div>

<div class="solution abs" style="left:92px"><h3>SOLUTION 1</h3><hr><p>Lorem ipsum dolor sit amet, consectetur adipisicing elit, sed do eiusmod tempor incididunt ut labore et</p><span class="more">MORE</span></div>
<div class="solution abs" style="left:234px"><h3>SOLUTION 2</h3><hr><p>Lorem ipsum dolor sit amet, consectetur adipisicing elit, sed do eiusmod tempor incididunt ut labore et</p><span class="more">MORE</span></div>
<div class="solution abs" style="left:376px"><h3>SOLUTION 3</h3><hr><p>Lorem ipsum dolor sit amet, consectetur adipisicing elit, sed do eiusmod tempor incididunt ut labore et</p><span class="more">MORE</span></div>
<div class="solution abs" style="left:518px"><h3>SOLUTION 4</h3><hr><p>Lorem ipsum dolor sit amet, consectetur adipisicing elit, sed do eiusmod tempor incididunt ut labore et</p><span class="more">MORE</span></div>

<blockquote class="quote abs" style="left:93px">The GRGC has allowed me to improve my website, become a published author and have confidence in what I do. My husband is now at peace about what his retirement will look like – HUGE!!</blockquote>
<svg class="quote-tail abs" style="left:203px" width="14" height="12" viewBox="0 0 14 12"><path d="M0 0h14L2 12z" fill="#f29a14"/></svg>
<span class="quote-name abs" style="left:111px">Rosalind P</span>

<blockquote class="quote abs" style="left:263px">I love the transformational processes and the structure the College offered. It enabled me to get out of my comfort zone and create a new business following my passion.</blockquote>
<svg class="quote-tail abs" style="left:373px" width="14" height="12" viewBox="0 0 14 12"><path d="M0 0h14L2 12z" fill="#f29a14"/></svg>
<span class="quote-name abs" style="left:281px">Delia M</span>

<div class="cta abs">
  <span class="cta-small abs">IF YOU ARE READY TO BECOME A</span>
  <span class="cta-big abs">GENTLE RIVER COACH</span>
  <span class="cta-button abs">CLICK HERE!</span>
</div>

<footer class="site-footer abs">
  <p class="footer-col abs" style="left:91px">GENTLE RIVER TRUST<br>P.O. BOX 718<br>FERNVALE QLD 4399</p>
  <p class="footer-col abs" style="left:188px">AUSTRALIA<br>PH: 07-5550-1234, FAX: 07-5550-9876<br>EMAIL: INFO@GENTLERIVERGUIDANCE.EXAMPLE</p>
  <div class="social abs"><span></span><span></span><span></span><span></span><span></span></div>
  <p class="footer-links abs">Affiliates | Affiliate Login | Media and Awards | Coaches Login (Previous) | Contact Us | Giving Back | Terms &amp; Conditions</p>
  <p class="copyright abs">© Copyright 2013. All Rights Reserved.</p>
</footer>

</body>
</html>
```